Harlow Brookworks highend custom homes

We build high end custom homes and timber frames we specialize in rustic hand made designs along with iron and concrete accents to add a modern touch 90% of my homes are buit on lake front properries attached is my logo and slogan as of now and my previous one

Target Market(s)

High end custom homes

Industry/Entity Type

Custom residential construction

Contact Information for Business Card

Been in buissness 8+ years inssured and reliable

Colors
A7469A
B969AE
D3A5CF
EDDBEB
F8F0F9

Requirements
Must have
• Must have slogan and phone number
Should not have
• A combination of rustic yet modern accents

```html
<!DOCTYPE html>
<html lang="en">
<head>
<meta charset="utf-8">
<title>Harlow Brookworks – Business Card</title>
<link href="https://fonts.googleapis.com/css2?family=Poppins:wght@400;600;700&family=Jost:wght@400&display=swap" rel="stylesheet">
<style>
  :root {
    --forest: #4b5c47;
    --forest-light: #56674f;
    --forest-dark: #45553f;
    --paper: #f6f6f4;
    --paper-shade: #ecedea;
    --ink: #1f1f1f;
    --white: #ffffff;
    --page: #ffffff;
  }
  * { margin: 0; padding: 0; box-sizing: border-box; }
  html, body {
    width: 742px; height: 1200px; overflow: hidden;
    background: var(--page);
  }
  .sheet {
    width: 742px; height: 1200px;
    display: flex; flex-direction: column; align-items: center; justify-content: center;
    gap: 86px;
  }
  .card {
    position: relative;
    width: 600px; height: 342px;
    overflow: hidden;
    box-shadow: 0 14px 34px rgba(0,0,0,0.22);
  }
  .card-backdrop { position: absolute; inset: 0; }
  .card--front .card-backdrop {
    background: radial-gradient(ellipse at 70% 30%, var(--forest-light), var(--forest) 55%, var(--forest-dark));
  }
  .card--back .card-backdrop {
    background: radial-gradient(ellipse at 70% 25%, var(--paper-shade), var(--paper) 60%);
  }

  /* Front */
  .front-brand {
    position: absolute; inset: 0;
    display: flex; flex-direction: column; align-items: center; justify-content: center;
    color: var(--white);
  }
  .brand-row { display: flex; align-items: center; gap: 14px; }
  .brand-mark { width: 22px; height: 22px; background: var(--white); }
  .brand-name {
    font-family: "Poppins", sans-serif; font-weight: 700;
    font-size: 34px; letter-spacing: 1px; text-transform: uppercase; line-height: 1;
  }
  .slogan {
    margin-top: 16px;
    font-family: "Jost", sans-serif; font-weight: 400;
    font-size: 15px; letter-spacing: 0.6px; text-transform: uppercase;
  }

  /* Back */
  .back-layout {
    position: absolute; inset: 0;
    display: flex; align-items: center; padding-left: 44px;
  }
  .back-brand { width: 196px; color: var(--forest); text-align: center; }
  .back-brand .brand-name { font-size: 21px; line-height: 1.15; color: var(--forest); }
  .back-brand .slogan { margin-top: 10px; font-size: 9.5px; color: var(--forest); }
  .divider { width: 2px; height: 180px; background: var(--forest); margin: 0 34px 0 20px; }
  .contact { color: var(--ink); font-family: "Poppins", sans-serif; }
  .person-name { font-weight: 600; font-size: 27px; line-height: 1; }
  .person-role { font-size: 13px; margin-bottom: 18px; }
  .contact-row { display: flex; align-items: center; gap: 12px; font-size: 14px; margin-top: 10px; white-space: nowrap; }
  .contact-icon {
    width: 28px; height: 28px; border-radius: 50%; background: var(--forest);
    display: flex; align-items: center; justify-content: center; flex: none;
  }
  .contact-icon svg { width: 15px; height: 15px; }
</style>
</head>
<body>
<main class="sheet">

  <section class="card card--front">
    <div class="card-backdrop" role="img" aria-label="Faded photograph of a large country house with trees, tinted forest green"></div>
    <div class="front-brand">
      <div class="brand-row">
        <span class="brand-mark"></span>
        <span class="brand-name">Harlow Brookworks</span>
      </div>
      <p class="slogan">• Built by lake and timber •</p>
    </div>
  </section>

  <section class="card card--back">
    <div class="card-backdrop" role="img" aria-label="Very faint photograph of a country house on a light background"></div>
    <div class="back-layout">
      <div class="back-brand">
        <p class="brand-name">Harlow<br>Brookworks</p>
        <p class="slogan">• Built by lake and timber •</p>
      </div>
      <div class="divider"></div>
      <div class="contact">
        <p class="person-name">Ellis Harrow</p>
        <p class="person-role">Founder</p>
        <p class="contact-row">
          <span class="contact-icon"><svg viewBox="0 0 24 24"><path fill="#fff" d="M6.6 10.8a15.1 15.1 0 0 0 6.6 6.6l2.2-2.2a1 1 0 0 1 1-.25 11.4 11.4 0 0 0 3.6.57 1 1 0 0 1 1 1V20a1 1 0 0 1-1 1A17 17 0 0 1 3 4a1 1 0 0 1 1-1h3.5a1 1 0 0 1 1 1c0 1.25.2 2.45.57 3.57a1 1 0 0 1-.25 1z"/></svg></span>
          (555) 014 2276
        </p>
        <p class="contact-row">
          <span class="contact-icon"><svg viewBox="0 0 24 24" fill="none" stroke="#fff" stroke-width="1.8"><rect x="3" y="6" width="18" height="12"/><path d="M3 6l9 7 9-7M3 18l7-6M21 18l-7-6"/></svg></span>
          hello@harlowbrookworks.com
        </p>
        <p class="contact-row">
          <span class="contact-icon"><svg viewBox="0 0 24 24" fill="none" stroke="#fff" stroke-width="1.6"><circle cx="12" cy="12" r="9"/><ellipse cx="12" cy="12" rx="4" ry="9"/><path d="M3 12h18M5 7h14M5 17h14"/></svg></span>
          www.harlowbrookworks.com
        </p>
      </div>
    </div>
  </section>

</main>
</body>
</html>
```